Looking for a modern website banner design

Bramblecrest Coaching Partners looking for the development of the main banner of the website. The project description and photos are included in the upload files.

```html
<!DOCTYPE html>
<html lang="en">
<head>
<meta charset="UTF-8">
<title>Bramblecrest Coaching Partners – Athlete Testimonial</title>
<link href="https://fonts.googleapis.com/css2?family=Poppins:ital,wght@0,400;0,600;1,300;1,500&display=swap" rel="stylesheet">
<style>
  :root {
    --panel-dark: #2d2d2f;
    --accent-blue: #1a73c4;
    --name-blue: #2196f3;
    --text-light: #ffffff;
    --crowd-dark: #2e2327;
    --crowd-warm: #5a3b3e;
    --boards-white: #e6e4de;
    --boards-yellow: #d6d16a;
    --ice-white: #f3f4f6;
  }
  * { margin: 0; padding: 0; box-sizing: border-box; }
  html, body { width: 1200px; height: 562px; overflow: hidden; background: #fff; }
  .banner {
    position: relative;
    width: 1200px;
    height: 562px;
    overflow: hidden;
    font-family: 'Poppins', sans-serif;
    color: var(--text-light);
  }
  .banner-shapes { position: absolute; inset: 0; }
  .testimonial {
    position: absolute;
    left: 46px;
    top: 72px;
    width: 370px;
    text-align: center;
  }
  .testimonial-quote {
    font-size: 19px;
    line-height: 26.3px;
    font-style: italic;
    font-weight: 300;
    letter-spacing: -0.1px;
  }
  .testimonial-quote strong { font-weight: 500; }
  .athlete-portrait {
    position: absolute;
    left: 166px;
    top: 283px;
    width: 128px;
    height: 128px;
    border-radius: 50%;
    background: linear-gradient(180deg, #6b5546 0%, #8a6f5e 45%, #2b3248 100%);
  }
  .athlete-name {
    position: absolute;
    left: 0;
    width: 460px;
    top: 426px;
    text-align: center;
    font-size: 19px;
    font-weight: 600;
    color: var(--name-blue);
  }
  .athlete-team {
    position: absolute;
    left: 0;
    width: 460px;
    top: 457px;
    text-align: center;
    font-size: 15px;
    line-height: 20px;
    font-weight: 400;
  }
</style>
</head>
<body>
<section class="banner">
  <svg class="banner-shapes" width="1200" height="562" viewBox="0 0 1200 562">
    <defs>
      <linearGradient id="actionPhotoTone" x1="0" y1="0" x2="0" y2="1">
        <stop offset="0" stop-color="var(--crowd-dark)"/>
        <stop offset="0.36" stop-color="var(--crowd-warm)"/>
        <stop offset="0.41" stop-color="var(--boards-white)"/>
        <stop offset="0.57" stop-color="var(--boards-white)"/>
        <stop offset="0.6" stop-color="var(--boards-yellow)"/>
        <stop offset="0.66" stop-color="var(--boards-yellow)"/>
        <stop offset="0.69" stop-color="var(--ice-white)"/>
        <stop offset="1" stop-color="#fbfbfc"/>
      </linearGradient>
    </defs>
    <rect class="action-photo" x="0" y="0" width="1200" height="562" fill="url(#actionPhotoTone)" role="img" aria-label="Photo of a hockey player celebrating a goal on the ice in front of a cheering crowd, with an opposing player skating past"/>
    <path class="accent-curve" d="M0 0 H520 C560 150 590 380 500 562 H0 Z" fill="var(--accent-blue)"/>
    <path class="panel-curve" d="M0 0 H400 C505 130 570 330 497 562 H0 Z" fill="var(--panel-dark)"/>
  </svg>

  <div class="testimonial">
    <p class="testimonial-quote">“<strong>Bramblecrest has provided support that has allowed me to develop as a person and an athlete.</strong> The S.T.R.I.D.E.™ process allowed me to stay focused on attainable goals each season and progress from Junior to College and now Professional Hockey.”</p>
  </div>

  <div class="athlete-portrait" role="img" aria-label="Portrait photo of the athlete in his hockey helmet"></div>
  <p class="athlete-name">Marcus Delaney</p>
  <p class="athlete-team">Riverton Gales<br>Eastern Seaboard Hockey League</p>
</section>
</body>
</html>
```